Design for social media advertising campaign

Multiple designs to be produced for a legal services advertising campaign in Australia offering assistance to small to medium sized businesses facing financial issues arising from the economic consequences of Covid-19. Designs must be sized suitably for LinkedIn, Twitter and Facebook. See our website recovery.harbourline.example and Facebook page KellowayLaw.CoastCounsel for logo, colours etc. Examples of the messaging is in the 5 uploaded files.

Target Market(s)

Small / medium size business owners

Industry/Entity Type

Legal

Requirements
Must have
• Sizing for Facebook, LinkedIn and Twitter

```html
<!DOCTYPE html>
<html lang="en">
<head>
<meta charset="utf-8">
<title>Kelloway Law – Structured to Survive</title>
<link rel="stylesheet" href="https://fonts.googleapis.com/css2?family=Poppins:wght@300;500;600;700&family=Tinos&display=swap">
<style>
  :root {
    --page-bg: #ffffff;
    --accent-gold: #ab9a66;
    --brand-red: #8a161b;
    --button-red: #86141a;
    --text-light: #ffffff;
    --photo-top: #3e4c54;
    --photo-mid: #23282b;
    --photo-sofa: #3a1f14;
    --photo-bottom: #0a0a0a;
  }
  * { margin: 0; padding: 0; box-sizing: border-box; }
  html, body {
    width: 1200px;
    height: 1000px;
    overflow: hidden;
    background: var(--page-bg);
  }
  .ad-card {
    position: absolute;
    left: 158px;
    top: 58px;
    width: 884px;
    height: 884px;
    overflow: hidden;
    box-shadow: 0 0 40px rgba(0, 0, 0, 0.06);
  }
  .gold-edge {
    position: absolute;
    left: 0; top: 0;
    width: 14px;
    height: 100%;
    background: var(--accent-gold);
    z-index: 3;
  }
  .hero-photo {
    position: absolute;
    left: 14px; top: 0;
    width: 870px;
    height: 100%;
    background:
      radial-gradient(ellipse 60% 30% at 50% 58%, rgba(90, 45, 28, 0.55), transparent 70%),
      linear-gradient(180deg, var(--photo-top) 0%, var(--photo-mid) 45%, var(--photo-sofa) 60%, var(--photo-bottom) 88%);
  }
  .brand-tab {
    position: absolute;
    right: 0; top: 0;
    width: 224px;
    height: 174px;
    z-index: 4;
  }
  .brand-tab svg { position: absolute; inset: 0; }
  .brand-mark {
    position: absolute;
    left: 86px; top: 24px;
    width: 40px; height: 40px;
    border-radius: 50%;
    background: var(--brand-red);
  }
  .brand-name {
    position: absolute;
    left: 34px; right: 0;
    top: 98px;
    text-align: center;
    font-family: "Poppins", sans-serif;
    font-weight: 500;
    font-size: 20px;
    color: var(--brand-red);
  }
  .brand-tagline {
    position: absolute;
    left: 34px; right: 0;
    top: 127px;
    text-align: center;
    font-family: "Tinos", serif;
    font-size: 15px;
    color: var(--brand-red);
  }
  .headline {
    position: absolute;
    left: 14px; right: 0;
    top: 410px;
    z-index: 2;
    text-align: center;
    color: var(--text-light);
    font-family: "Poppins", sans-serif;
  }
  .headline-lead {
    display: block;
    font-weight: 700;
    font-size: 50px;
    line-height: 64px;
    letter-spacing: -0.5px;
    padding-left: 8px;
  }
  .headline-key {
    display: inline-block;
    margin-top: 14px;
    width: 526px;
    height: 98px;
    border: 6px solid var(--brand-red);
    font-weight: 300;
    font-size: 62px;
    line-height: 86px;
    letter-spacing: 1px;
    margin-left: 4px;
  }
  .headline-close {
    display: block;
    margin-top: 4px;
    font-weight: 700;
    font-size: 70px;
    line-height: 86px;
    padding-left: 8px;
  }
  .offer {
    position: absolute;
    left: 14px; right: 0;
    top: 712px;
    z-index: 2;
    text-align: center;
    font-family: "Poppins", sans-serif;
    font-weight: 500;
    font-size: 25px;
    color: var(--text-light);
    padding-left: 8px;
  }
  .cta-button {
    position: absolute;
    left: 334px; top: 762px;
    width: 245px; height: 78px;
    z-index: 2;
    background: var(--button-red);
    border-radius: 3px;
    text-align: center;
    font-family: "Poppins", sans-serif;
    font-weight: 600;
    font-size: 42px;
    line-height: 78px;
    color: var(--text-light);
  }
</style>
</head>
<body>
  <main class="ad-card">
    <div class="gold-edge"></div>
    <div class="hero-photo" role="img" aria-label="Stressed business owner sitting on a brown leather sofa with his hand over his eyes, against a dark slate wall"></div>

    <header class="brand-tab">
      <svg width="224" height="174" viewBox="0 0 224 174" aria-hidden="true">
        <polygon points="0,0 224,0 224,174 34,165" fill="#ffffff"/>
      </svg>
      <span class="brand-mark" aria-hidden="true"></span>
      <p class="brand-name">Kelloway Law</p>
      <p class="brand-tagline">Barristers &amp; Solicitors</p>
    </header>

    <h1 class="headline">
      <span class="headline-lead">Is your business</span>
      <span class="headline-key">STRUCTURED</span>
      <span class="headline-close">TO SURVIVE?</span>
    </h1>

    <p class="offer">obtain our free guide</p>
    <a class="cta-button">NOW</a>
  </main>
</body>
</html>
```